Brambury Logistics

Create a modern, simple, Elegant business card design for my business.

Services: Tamo Trucks, Transport, Contract Logistics,

Industry/Entity Type

Business

Contact Information for Business Card

Include all details same as old card plus new website address: www.bramburylogistics.com.au

Requirements
Must have
• Similar colors to Logo.

```html
<!DOCTYPE html>
<html lang="en">
<head>
<meta charset="utf-8">
<title>Brambury Logistics – Business Card</title>
<link rel="stylesheet" href="https://fonts.googleapis.com/css2?family=Montserrat:wght@400;500;600;700&display=swap">
<style>
  :root {
    --bg: #e9e7e3;
    --card-white: #ffffff;
    --ink: #4a4c50;
    --ink-soft: #7b7e83;
    --brand-blue: #1f6aa5;
    --bright-blue: #2c9fe2;
    --dark-top: #4a4c50;
    --dark-bottom: #16171a;
    --logo-grey: #8d9095;
  }
  * { box-sizing: border-box; margin: 0; padding: 0; }
  html, body { width: 1200px; height: 913px; overflow: hidden; }
  body {
    background: var(--bg);
    font-family: "Montserrat", sans-serif;
    position: relative;
  }
  .card {
    position: absolute;
    width: 540px;
    height: 310px;
    border-radius: 16px;
    overflow: hidden;
    box-shadow: 0 6px 18px rgba(0,0,0,.18);
  }

  /* Front */
  .card-front { left: 70px; top: 120px; background: var(--card-white); }
  .card-front .corner-band {
    position: absolute; right: 0; bottom: 0;
    width: 120px; height: 170px;
    background: var(--brand-blue);
  }
  .front-logo {
    position: absolute; left: 34px; top: 38px;
    display: flex; align-items: center; gap: 10px;
  }
  .logo-mark {
    width: 18px; height: 18px; border-radius: 50%;
    background: var(--brand-blue);
  }
  .logo-name {
    font-weight: 700; font-size: 30px; color: var(--brand-blue);
    letter-spacing: .5px;
  }
  .tagline {
    position: absolute; left: 36px; top: 92px;
    font-size: 10.5px; font-weight: 500; color: var(--ink-soft);
    letter-spacing: 1px; text-transform: uppercase;
  }
  .person { position: absolute; left: 36px; top: 150px; }
  .person-name { font-size: 22px; font-weight: 600; color: var(--ink); }
  .person-role { font-size: 13px; color: var(--brand-blue); margin-top: 2px; }
  .contacts { position: absolute; left: 36px; top: 214px; list-style: none; }
  .contacts li {
    display: flex; align-items: center; gap: 10px;
    font-size: 13px; color: var(--brand-blue); line-height: 22px;
  }
  .contacts svg { width: 11px; height: 11px; fill: var(--ink); }

  /* Back */
  .card-back {
    left: 590px; top: 480px;
    background: linear-gradient(160deg, var(--dark-top), var(--dark-bottom) 70%);
  }
  .back-logo {
    position: absolute; left: 60px; top: 60px;
    display: flex; align-items: center; gap: 10px;
  }
  .back-logo .logo-mark { background: var(--bright-blue); }
  .back-logo .logo-name { color: var(--logo-grey); font-size: 34px; }
  .services {
    position: absolute; left: 150px; top: 140px; list-style: none;
  }
  .services li {
    position: relative; padding-left: 16px;
    font-size: 15px; color: var(--bright-blue); line-height: 25px;
  }
  .services li::before {
    content: ""; position: absolute; left: 0; top: 10px;
    width: 6px; height: 6px; border-radius: 50%; background: var(--bright-blue);
  }
</style>
</head>
<body>

<section class="card card-front" aria-label="Business card front">
  <div class="corner-band"></div>
  <div class="front-logo">
    <span class="logo-mark"></span>
    <span class="logo-name">Brambury Logistics</span>
  </div>
  <p class="tagline">Tamo Trucks - Transport - Contract Logistics</p>
  <div class="person">
    <p class="person-name">Marcus Ellery</p>
    <p class="person-role">Director</p>
  </div>
  <ul class="contacts">
    <li>
      <svg viewBox="0 0 24 24"><path d="M6.6 10.8a15 15 0 0 0 6.6 6.6l2.2-2.2c.3-.3.7-.4 1-.2 1.1.4 2.3.6 3.6.6.6 0 1 .4 1 1V20c0 .6-.4 1-1 1A17 17 0 0 1 3 4c0-.6.4-1 1-1h3.5c.6 0 1 .4 1 1 0 1.3.2 2.5.6 3.6.1.3 0 .7-.2 1z"/></svg>
      0412 555 038
    </li>
    <li>
      <svg viewBox="0 0 24 24"><path d="M2 5h20v14H2zm2 2v.5l8 5 8-5V7zm0 2.8V17h16V9.8l-8 5z"/></svg>
      marcus@bramburylogistics.com.au
    </li>
    <li>
      <svg viewBox="0 0 24 24"><path d="M12 2a10 10 0 1 0 0 20 10 10 0 0 0 0-20zm6.9 9h-3a15 15 0 0 0-1.3-5.6A8 8 0 0 1 18.9 11zM12 4.1c.9 1.3 1.7 3.6 1.9 6.9h-3.8c.2-3.3 1-5.6 1.9-6.9zM9.4 5.4A15 15 0 0 0 8.1 11h-3a8 8 0 0 1 4.3-5.6zM5.1 13h3a15 15 0 0 0 1.3 5.6A8 8 0 0 1 5.1 13zm6.9 6.9c-.9-1.3-1.7-3.6-1.9-6.9h3.8c-.2 3.3-1 5.6-1.9 6.9zm2.6-1.3a15 15 0 0 0 1.3-5.6h3a8 8 0 0 1-4.3 5.6z"/></svg>
      www.bramburylogistics.com.au
    </li>
  </ul>
</section>

<section class="card card-back" aria-label="Business card back">
  <div class="back-logo">
    <span class="logo-mark"></span>
    <span class="logo-name">Brambury Logistics</span>
  </div>
  <ul class="services">
    <li>Tamo Trucks</li>
    <li>All General and Oversize Transport</li>
    <li>Specialized Transport</li>
    <li>Contract Logistics</li>
    <li>Express/Hotshot Services</li>
  </ul>
</section>

</body>
</html>
```